Marlow Family Chiropractic Stationary

The letterhead and business card must have our logo.
We would like to see the logo used in different ways ( It can be expanded upon in the stationary.)
Please use the the same or similar colors.
Must be eye catching and memorable.
Must be easy to read

Reason: The doctor has been too busy to make any final decisions. He would like to give himself a little more time.

Target Market(s)

Chiropractic Healthcare

Industry/Entity Type

Business

Requirements
Must have
• Dr. Nathaniel Marlow D.C.
Chiropractor

207-555-0193

415 Birchwood Parkway, 2nd Floor
Larkfield, ME 04999

drmarlow@marlowspine.example
www.marlowspine.example
www.facebook.com/MarlowFamilySpine
Should not have
• should not be difficult to read

```html
<!DOCTYPE html>
<html lang="en">
<head>
<meta charset="utf-8">
<title>Marlow Family Chiropractic – Business Cards</title>
<link href="https://fonts.googleapis.com/css2?family=Montserrat:wght@700&family=Questrial&family=Arimo:wght@400&display=swap" rel="stylesheet">
<style>
  :root {
    --backdrop: #6b3a24;
    --card-black: #000000;
    --leaf-green: #a6cc5c;
    --band-green: #a8cf5e;
    --taupe: #8d8178;
    --white: #ffffff;
    --ink: #1a1a1a;
    --pattern-dark: #14170c;
    --pattern-mid: #2a3115;
  }
  * { margin: 0; padding: 0; box-sizing: border-box; }
  html, body { width: 1200px; height: 716px; overflow: hidden; }
  body { background: var(--backdrop); position: relative; font-family: "Arimo", Arial, sans-serif; }

  .card {
    position: absolute;
    width: 524px;
    height: 299px;
    border-radius: 18px;
    overflow: hidden;
  }
  .card--front { left: 41px; top: 35px; background: var(--card-black); }
  .card--mark-dark { left: 598px; top: 33px; background: var(--card-black); }
  .card--pattern { left: 41px; top: 359px; background: var(--card-black); }
  .card--mark-green { left: 598px; top: 354px; background: var(--band-green); }

  .wordmark {
    position: absolute;
    left: 0; right: 0;
    text-align: center;
    font-family: "Montserrat", Arial, sans-serif;
    font-weight: 700;
    text-transform: uppercase;
    line-height: 1;
  }
  .wordmark__name { display: block; }
  .wordmark__sub { display: block; }

  .card--front .wordmark { top: 14px; color: var(--leaf-green); }
  .card--front .wordmark__dot {
    display: block; width: 90px; height: 90px; border-radius: 50%;
    background: var(--leaf-green); margin: 0 auto 12px;
  }
  .card--front .wordmark__name { font-size: 26px; letter-spacing: .5px; }
  .card--front .wordmark__sub { font-size: 11px; letter-spacing: .5px; margin-top: 3px; }

  .rule-top {
    position: absolute; left: 0; right: 0; top: 169px; height: 2px;
    background: var(--band-green);
  }
  .contact-band {
    position: absolute; left: 0; right: 0; top: 173px; height: 91px;
    background: var(--band-green);
    color: var(--ink);
    font-size: 13px;
  }
  .address {
    position: absolute; right: 283px; top: 13px;
    text-align: right; line-height: 21px; letter-spacing: .3px; font-style: normal;
  }
  .band-divider {
    position: absolute; left: 253px; top: 6px; width: 1px; height: 78px;
    background: rgba(0,0,0,.45);
  }
  .contact-list {
    position: absolute; left: 264px; top: 2px;
    list-style: none; line-height: 21px; letter-spacing: .2px;
  }
  .contact-list li { display: flex; align-items: center; gap: 6px; }
  .contact-list svg { width: 11px; height: 11px; flex: none; }
  .contact-list .fb-square { width: 10px; height: 10px; background: #3b5998; border-radius: 2px; flex: none; }

  .doctor-line {
    position: absolute; left: 0; right: 0; top: 276px;
    text-align: center; color: var(--leaf-green); font-size: 14px;
  }
  .doctor-line .role { color: var(--taupe); font-size: 12.5px; }

  .card--mark-dark .wordmark { top: 86px; color: var(--leaf-green); }
  .card--mark-green .wordmark { top: 86px; color: var(--white); }
  .card--mark-dark .wordmark__name,
  .card--mark-green .wordmark__name { font-size: 42px; letter-spacing: 2px; }
  .card--mark-dark .wordmark__sub,
  .card--mark-green .wordmark__sub { font-size: 15px; letter-spacing: 1.5px; margin-top: 10px; }

  .web {
    position: absolute; left: 0; right: 0; top: 261px;
    text-align: center;
    font-family: "Questrial", Arial, sans-serif;
    font-size: 15px; letter-spacing: 2.4px;
    color: var(--white);
  }

  .pattern-fill {
    position: absolute; inset: 0;
    background: radial-gradient(ellipse at center, var(--pattern-mid) 0%, var(--pattern-dark) 70%, var(--card-black) 100%);
  }
  .card--pattern .wordmark { top: 96px; color: var(--leaf-green); }
  .card--pattern .wordmark__name { font-size: 64px; letter-spacing: 3px; }
  .card--pattern .wordmark__sub { font-size: 25px; letter-spacing: 1px; margin-top: 10px; }
</style>
</head>
<body>

<section class="card card--front" aria-label="Business card front">
  <div class="wordmark">
    <span class="wordmark__dot"></span>
    <span class="wordmark__name">Marlow</span>
    <span class="wordmark__sub">Family Chiropractic</span>
  </div>
  <div class="rule-top"></div>
  <div class="contact-band">
    <address class="address">
      415 Birchwood Parkway<br>2nd Floor<br>Larkfield, ME 04999
    </address>
    <div class="band-divider"></div>
    <ul class="contact-list">
      <li>
        <svg viewBox="0 0 12 12" aria-hidden="true"><path d="M2.5 1 L4.5 1 L5.3 3.6 L4 4.6 C4.8 6.3 5.7 7.2 7.4 8 L8.4 6.7 L11 7.5 L11 9.5 C11 10.3 10.3 11 9.5 11 C5 11 1 7 1 2.5 C1 1.7 1.7 1 2.5 1 Z" fill="#1a1a1a"/></svg>
        207-555-0193
      </li>
      <li>
        <svg viewBox="0 0 12 12" aria-hidden="true"><rect x="1" y="2.5" width="10" height="7" rx="1" fill="#1a1a1a"/><path d="M1.5 3 L6 6.5 L10.5 3" stroke="#a8cf5e" stroke-width="1" fill="none"/></svg>
        drmarlow@marlowspine.example
      </li>
      <li>
        <svg viewBox="0 0 12 12" aria-hidden="true"><circle cx="6" cy="6" r="5" fill="none" stroke="#1a1a1a" stroke-width="1.2"/><ellipse cx="6" cy="6" rx="2.2" ry="5" fill="none" stroke="#1a1a1a" stroke-width="1"/><path d="M1 6 H11" stroke="#1a1a1a" stroke-width="1"/></svg>
        www.marlowspine.example
      </li>
      <li>
        <span class="fb-square" aria-hidden="true"></span>
        MarlowFamilySpine
      </li>
    </ul>
  </div>
  <p class="doctor-line">Dr. Nathaniel Marlow D.C., <span class="role">Chiropractor</span></p>
</section>

<section class="card card--mark-dark" aria-label="Business card back, dark">
  <div class="wordmark">
    <span class="wordmark__name">Marlow</span>
    <span class="wordmark__sub">Family Chiropractic</span>
  </div>
  <p class="web">www.marlowspine.example</p>
</section>

<section class="card card--pattern" aria-label="Business card back, patterned">
  <div class="pattern-fill" role="img" aria-label="Repeating pattern of small dark tree motifs"></div>
  <div class="wordmark">
    <span class="wordmark__name">Marlow</span>
    <span class="wordmark__sub">Family Chiropractic</span>
  </div>
  <p class="web">www.marlowspine.example</p>
</section>

<section class="card card--mark-green" aria-label="Business card back, green">
  <div class="wordmark">
    <span class="wordmark__name">Marlow</span>
    <span class="wordmark__sub">Family Chiropractic</span>
  </div>
  <p class="web">www.marlowspine.example</p>
</section>

</body>
</html>
```